BUSINESS CARD - HALVERDINE RURAL SERVICES

I would like to create a business card for my fertilizer spreading business. I would like to incorporate my existing logo and also a description of the services offered. The business card will be given to farmers so must be kept simple but effective. It will also be left in stores so much also be eye catching in order to stand out from other cards.

Target Market(s)

FARMERS

Requirements
Must have
• FRONT OF CARD = EXISTING LOGO + "CUSTOMISED SPREADING" below the logo

REAR Of CARD = SERVICES OFFERED AND CONTACT DETAILS

- Bulk fertilizer including Lime, Gypsum, Manure & Compost
- Granular fertilizer including Single Super, Urea, Gran-am, & Custom Blends
- Modern equipment - Autosteer & Variable Rate Capable
- Friendly & Reliable Service
- Contact Gus: 0471 502 318
Nice to have
• utilize same color scheme as existing logo

```html
<!DOCTYPE html>
<html lang="en">
<head>
<meta charset="utf-8">
<title>Halverdine Rural Services – Business Card</title>
<link rel="stylesheet" href="https://fonts.googleapis.com/css2?family=Open+Sans:wght@600;700&family=Arimo:wght@400;700&display=swap">
<style>
  :root {
    --backdrop: #d7d5d6;
    --card-white: #ffffff;
    --slate: #58585a;
    --ink: #4d4d4f;
    --orange: #f7931e;
  }
  * { margin: 0; padding: 0; box-sizing: border-box; }
  html, body {
    width: 1200px;
    height: 1100px;
    overflow: hidden;
    background: var(--backdrop);
  }
  .card {
    position: absolute;
    left: 259px;
    width: 705px;
    height: 405px;
    border-radius: 20px;
    overflow: hidden;
    box-shadow: 0 2px 6px rgba(0,0,0,0.25);
  }
  .card--rear { top: 114px; background: var(--card-white); }
  .card--front { top: 560px; background: var(--slate); }

  .services-title {
    position: absolute;
    left: 42px;
    top: 38px;
    font-family: "Open Sans", sans-serif;
    font-weight: 600;
    font-size: 26px;
    color: var(--orange);
    letter-spacing: 0.2px;
  }
  .services-list {
    position: absolute;
    left: 42px;
    top: 75px;
    list-style: none;
    font-family: "Arimo", sans-serif;
    font-size: 17px;
    line-height: 24px;
    color: var(--ink);
  }
  .services-list li::before {
    content: "•";
    color: var(--orange);
    margin-right: 3px;
  }

  .decor-arc {
    position: absolute;
    left: 0;
    top: 0;
  }

  .contact-label {
    position: absolute;
    right: 40px;
    top: 274px;
    font-family: "Arimo", sans-serif;
    font-weight: 700;
    font-size: 30px;
    color: var(--ink);
  }
  .phone-band {
    position: absolute;
    left: 0;
    top: 0;
  }
  .phone-number {
    position: absolute;
    left: 395px;
    top: 320px;
    font-family: "Arimo", sans-serif;
    font-size: 34px;
    color: var(--card-white);
    letter-spacing: 0.5px;
  }

  .brand-mark {
    position: absolute;
    left: 0;
    top: 0;
  }
  .brand-name {
    position: absolute;
    left: 0;
    width: 100%;
    top: 210px;
    text-align: center;
    font-family: "Open Sans", sans-serif;
    font-weight: 700;
    font-size: 29px;
    color: var(--card-white);
  }
  .tagline {
    position: absolute;
    left: 0;
    width: 100%;
    top: 340px;
    text-align: center;
    font-family: "Open Sans", sans-serif;
    font-weight: 600;
    font-size: 23px;
    color: var(--orange);
  }
</style>
</head>
<body>

<section class="card card--rear">
  <svg class="decor-arc" width="705" height="405" viewBox="0 0 705 405" aria-hidden="true">
    <circle cx="113" cy="306" r="114" fill="none" stroke="var(--slate)" stroke-width="6"/>
  </svg>

  <h2 class="services-title">SERVICES OFFERED</h2>
  <ul class="services-list">
    <li>Bulk fertilizer including Lime, Gypsum, Manure &amp; Compost</li>
    <li>Granular fertilizer including Single Super, Urea, Gran-am, &amp; Custom Blends</li>
    <li>Modern equipment - Autosteer &amp; Variable Rate Capable</li>
    <li>Friendly &amp; Reliable Service</li>
  </ul>

  <p class="contact-label">Contact Gus:</p>
  <svg class="phone-band" width="705" height="405" viewBox="0 0 705 405" aria-hidden="true">
    <polygon points="329,368 386,317 705,318 705,369" fill="var(--slate)"/>
    <path d="M641 329 l6 -2 l5 9 l-4 4 q3 7 9 10 l4 -4 l8 5 l-2 6 q-3 3 -9 1 q-15 -7 -20 -20 q-1 -6 3 -9 z" fill="var(--orange)"/>
  </svg>
  <p class="phone-number">0471 502 318</p>
</section>

<section class="card card--front">
  <svg class="brand-mark" width="705" height="405" viewBox="0 0 705 405" aria-hidden="true">
    <circle cx="352" cy="125" r="72" fill="none" stroke="var(--card-white)" stroke-width="5"/>
  </svg>
  <h1 class="brand-name">Halverdine Rural Services</h1>
  <p class="tagline">CUSTOMISED SPREADING</p>
</section>

</body>
</html>
```